Penrow Insights - what matters when choosing suppliers

We are a consultancy firm called Penrow Insights specializing in customer strategies. We would like to a more illustrative design of the attached graphic.

The graph shows what is important for B2B companies when choosing suppliers. On the left we have the statistical importance and on the right we have the "asked" importance ("on a scale from 1-10, how important is...." ).

Hope it makes sense! :-)

Target Market(s)

B2B Companies

Industry/Entity Type

Business Consultant

```html
<!DOCTYPE html>
<html lang="en">
<head>
<meta charset="utf-8">
<title>Importance of business drivers</title>
<link rel="stylesheet" href="https://fonts.googleapis.com/css2?family=Source+Sans+3:ital,wght@0,400;0,700;1,400&display=swap">
<style>
  :root {
    --ink: #2c4a52;
    --bg: #ffffff;
    --track: #f4f4f4;
    --track-edge: #d6d6d6;
    --tick: #8a8a8a;
    --target: #e0607a;
    --calc-top: #a3b1b3;
    --calc-bottom: #3d5a62;
    --asked-top: #86a8df;
    --asked-bottom: #4a77c6;
    --marker-edge: #c4c4c4;
  }
  html, body {
    margin: 0;
    width: 1200px;
    height: 900px;
    overflow: hidden;
    background: var(--bg);
    font-family: "Source Sans 3", sans-serif;
    color: var(--ink);
  }
  .figure {
    position: relative;
    width: 1200px;
    height: 900px;
  }
  .figure-title {
    position: absolute;
    left: 226px;
    top: 207px;
    margin: 0;
    font-size: 21px;
    font-weight: 700;
  }
  .chart {
    position: absolute;
    left: 0;
    top: 0;
  }
  .column-heading {
    font-size: 19px;
    font-weight: 700;
    fill: var(--ink);
  }
  .driver-label {
    font-size: 18px;
    fill: var(--ink);
  }
  .footnotes {
    position: absolute;
    left: 226px;
    top: 618px;
    width: 760px;
    margin: 0;
    font-style: italic;
    font-size: 16px;
    line-height: 20px;
  }
  .footnotes p { margin: 0 0 14px; }
</style>
</head>
<body>
<main class="figure">
  <h1 class="figure-title">Figure 1. Importance of business drivers</h1>

  <svg class="chart" width="1200" height="900" viewBox="0 0 1200 900" aria-label="Calculated and asked importance of five business drivers">
    <defs>
      <linearGradient id="calc-fill" x1="0" y1="0" x2="0" y2="1">
        <stop offset="0" stop-color="var(--calc-top)"/>
        <stop offset="1" stop-color="var(--calc-bottom)"/>
      </linearGradient>
      <linearGradient id="asked-fill" x1="0" y1="0" x2="0" y2="1">
        <stop offset="0" stop-color="var(--asked-top)"/>
        <stop offset="1" stop-color="var(--asked-bottom)"/>
      </linearGradient>
      <g id="marker">
        <path d="M-4 23 V-2 L0 -8 L4 -2 V23 Z" fill="#fff" stroke="var(--marker-edge)" stroke-width="1"/>
        <rect x="-1.5" y="9" width="3" height="4" fill="none" stroke="var(--marker-edge)" stroke-width="0.8"/>
      </g>
      <g id="ticks" stroke="var(--tick)" stroke-width="1">
        <line x1="0" y1="0" x2="0" y2="6"/><line x1="28.3" y1="0" x2="28.3" y2="6"/>
        <line x1="56.6" y1="0" x2="56.6" y2="6"/><line x1="84.9" y1="0" x2="84.9" y2="6"/>
        <line x1="113.2" y1="0" x2="113.2" y2="6"/><line x1="141.5" y1="0" x2="141.5" y2="6"/>
        <line x1="169.8" y1="0" x2="169.8" y2="6"/><line x1="198.1" y1="0" x2="198.1" y2="6"/>
        <line x1="226.4" y1="0" x2="226.4" y2="6"/><line x1="254.7" y1="0" x2="254.7" y2="6"/>
        <line x1="283" y1="0" x2="283" y2="6"/>
      </g>
    </defs>

    <text class="column-heading" x="367" y="281" text-anchor="middle">Calculated importance*</text>
    <text class="column-heading" x="833" y="281" text-anchor="middle">Asked importance**</text>

    <!-- calculated importance -->
    <g class="calc-chart">
      <use href="#ticks" x="226" y="304"/>
      <g fill="var(--track)" stroke="var(--track-edge)">
        <rect x="226.5" y="320.5" width="283" height="22"/>
        <rect x="226.5" y="375.5" width="283" height="22"/>
        <rect x="226.5" y="429.5" width="283" height="22"/>
        <rect x="226.5" y="484.5" width="283" height="22"/>
        <rect x="226.5" y="539.5" width="283" height="22"/>
      </g>
      <g fill="url(#calc-fill)">
        <rect x="253" y="320" width="256" height="23"/>
        <rect x="279" y="375" width="230" height="23"/>
        <rect x="419" y="429" width="90" height="23"/>
        <rect x="435" y="484" width="74" height="23"/>
        <rect x="503" y="539" width="6" height="23"/>
      </g>
      <line x1="396.5" y1="304" x2="396.5" y2="584" stroke="var(--target)" stroke-width="1" stroke-dasharray="4 3"/>
      <use href="#marker" x="253" y="320"/>
      <use href="#marker" x="279" y="375"/>
      <use href="#marker" x="419" y="429"/>
      <use href="#marker" x="435" y="484"/>
      <use href="#marker" x="503" y="539"/>
    </g>

    <!-- asked importance -->
    <g class="asked-chart">
      <use href="#ticks" x="691" y="304"/>
      <g fill="var(--track)" stroke="var(--track-edge)">
        <rect x="691.5" y="320.5" width="283" height="22"/>
        <rect x="691.5" y="375.5" width="283" height="22"/>
        <rect x="691.5" y="429.5" width="283" height="22"/>
        <rect x="691.5" y="484.5" width="283" height="22"/>
        <rect x="691.5" y="539.5" width="283" height="22"/>
      </g>
      <g fill="url(#asked-fill)">
        <rect x="691" y="320" width="195" height="23"/>
        <rect x="691" y="375" width="13" height="23"/>
        <rect x="691" y="429" width="125" height="23"/>
        <rect x="691" y="484" width="261" height="23"/>
        <rect x="691" y="539" width="137" height="23"/>
      </g>
      <line x1="804.5" y1="304" x2="804.5" y2="584" stroke="var(--target)" stroke-width="1" stroke-dasharray="4 3"/>
      <use href="#marker" x="886" y="320"/>
      <use href="#marker" x="704" y="375"/>
      <use href="#marker" x="816" y="429"/>
      <use href="#marker" x="952" y="484"/>
      <use href="#marker" x="828" y="539"/>
    </g>

    <g class="driver-labels" text-anchor="middle">
      <text class="driver-label" x="598" y="341">Products</text>
      <text class="driver-label" x="598" y="396">Brand</text>
      <text class="driver-label" x="598" y="450">Advice</text>
      <text class="driver-label" x="598" y="505">Delivery</text>
      <text class="driver-label" x="598" y="547">Customer</text>
      <text class="driver-label" x="598" y="566">service</text>
    </g>
  </svg>

  <div class="footnotes">
    <p>*Calculated importance is found through statistical analysis. Partial Least Squares is used to discover the connection between each business driver and loyalty.</p>
    <p>**Asked importance is found by simply asking customers how important they find each business driver.</p>
  </div>
</main>
</body>
</html>
```